Label Design for Nuts package*

Develop the design for a label for nuts sold in a paperbag.

you can find our website here: www.kornfeld-snack.de.
Here comes the link to our catalogue: https://www.blattwerk-docs.com/de/document/read/48172956/kornfeld-premium-snacks-gesamtkatalog-2019

With this product we are targeting private customers who want to buy nuts with plastic free packaging online.
The colours of the label should fit the brown paper bag.

```html
<!DOCTYPE html>
<html lang="de">
<head>
<meta charset="utf-8">
<title>Kornfeld Nuts – Etikett</title>
<link rel="stylesheet" href="https://fonts.googleapis.com/css2?family=Roboto+Slab:wght@200;300;700&display=swap">
<style>
  :root {
    --cocoa: #55291f;
    --caramel: #a55b2c;
    --white: #ffffff;
    --brand-ink: #5a2b22;
    --tagline: #b4683c;
    --kraft: #d7b16c;
    --kraft-dark: #c89d55;
    --nut-light: #e7d8d2;
    --nut: #b67a55;
    --page: #ffffff;
  }
  html, body { margin: 0; padding: 0; width: 1200px; height: 1200px; overflow: hidden; background: var(--page); }
  .board { display: block; width: 1200px; height: 1200px; font-family: "Roboto Slab", Georgia, serif; }
  .label-cocoa .label-body { fill: var(--cocoa); }
  .label-caramel .label-body { fill: var(--caramel); }
  .brand-panel { fill: var(--white); }
  .brand-panel-rule { fill: none; stroke: var(--brand-ink); stroke-width: 1.2; opacity: .6; }
  .brand-name { font-family: "Roboto Slab", Georgia, serif; font-weight: 300; font-size: 46px; fill: var(--brand-ink); letter-spacing: 3px; }
  .brand-dot { fill: var(--brand-ink); }
  .brand-tagline { font-family: "Roboto Slab", Georgia, serif; font-weight: 300; font-size: 14px; fill: var(--tagline); letter-spacing: 3px; }
  .brand-line { stroke: var(--tagline); stroke-width: 1.4; }
  .product-title { font-family: "Roboto Slab", Georgia, serif; font-weight: 200; font-size: 112px; fill: var(--white); letter-spacing: 2px; }
  .variety-band { fill: var(--white); opacity: .13; }
  .variety-name { font-family: "Roboto Slab", Georgia, serif; font-weight: 700; font-size: 27px; fill: var(--white); letter-spacing: 3.5px; }
  .variety-note { font-family: "Roboto Slab", Georgia, serif; font-weight: 300; font-size: 17px; fill: var(--white); opacity: .9; }
  .bag { fill: var(--kraft); }
  .bag-seam { fill: var(--kraft-dark); }
  .bag-window { fill: url(#nutGradient); }
</style>
</head>
<body>
<svg class="board" viewBox="0 0 1800 1800" xmlns="http://www.w3.org/2000/svg" aria-label="Kornfeld Nuts Etiketten und Beutel">
  <defs>
    <linearGradient id="nutGradient" x1="0" x2="1" y1="0" y2="0">
      <stop offset="0" stop-color="var(--nut-light)"/>
      <stop offset=".2" stop-color="var(--nut)"/>
      <stop offset=".8" stop-color="var(--nut)"/>
      <stop offset="1" stop-color="var(--nut-light)"/>
    </linearGradient>

    <symbol id="label-arched" viewBox="0 0 486 678">
      <g class="label-cocoa">
        <path class="label-body" d="M0 0 H486 V435 A243 243 0 0 1 0 435 Z"/>
        <path class="brand-panel" d="M69 76 H150 C182 30 304 30 336 76 H417 V262 H336 C304 312 182 312 150 262 H69 Z"/>
        <path class="brand-panel-rule" d="M74 81 H153 C184 38 302 38 333 81 H412 V257 H333 C302 304 184 304 153 257 H74 Z"/>
        <circle class="brand-dot" cx="243" cy="122" r="14"/>
        <text class="brand-name" x="243" y="200" text-anchor="middle">kornfeld</text>
        <text class="brand-tagline" x="243" y="226" text-anchor="middle">PREMIUM SNACKS</text>
        <line class="brand-line" x1="160" y1="236" x2="326" y2="236"/>
        <text class="product-title" x="243" y="430" text-anchor="middle">NUTS</text>
        <rect class="variety-band" x="79" y="456" width="338" height="110"/>
        <text class="variety-name" x="248" y="500" text-anchor="middle">CASHEWKERNE</text>
        <text class="variety-note" x="248" y="528" text-anchor="middle">gerostet mit Net</text>
        <text class="variety-note" x="248" y="549" text-anchor="middle">&amp; Weinbeeren getrocknet</text>
      </g>
    </symbol>

    <symbol id="label-boxed" viewBox="0 0 486 678">
      <g class="label-caramel">
        <path class="label-body" d="M0 0 H486 V435 A243 243 0 0 1 0 435 Z"/>
        <rect class="brand-panel" x="69" y="71" width="350" height="186"/>
        <circle class="brand-dot" cx="243" cy="118" r="14"/>
        <text class="brand-name" x="243" y="193" text-anchor="middle">kornfeld</text>
        <text class="brand-tagline" x="243" y="220" text-anchor="middle">PREMIUM SNACKS</text>
        <line class="brand-line" x1="160" y1="230" x2="326" y2="230"/>
        <text class="product-title" x="243" y="388" text-anchor="middle" style="font-size:118px">NUTS</text>
        <rect class="variety-band" x="79" y="424" width="338" height="109"/>
        <text class="variety-name" x="248" y="468" text-anchor="middle">CASHEWKERNE</text>
        <text class="variety-note" x="248" y="495" text-anchor="middle">gerostet mit Net</text>
        <text class="variety-note" x="248" y="516" text-anchor="middle">&amp; Weinbeeren getrocknet</text>
      </g>
    </symbol>
  </defs>

  <!-- flat labels -->
  <use href="#label-arched" x="296" y="162" width="486" height="678"/>
  <use href="#label-boxed" x="887" y="162" width="486" height="678"/>

  <!-- pouch with arched label -->
  <g class="pouch">
    <rect class="bag" x="317" y="948" width="458" height="717" role="img" aria-label="Kraftpapier-Standbeutel"/>
    <rect class="bag-seam" x="317" y="948" width="458" height="8"/>
    <use href="#label-arched" x="419" y="948" width="256" height="357"/>
    <rect class="bag-window" x="360" y="1340" width="375" height="135" role="img" aria-label="Cashewkerne im Sichtfenster"/>
  </g>

  <!-- pouch with boxed label -->
  <g class="pouch">
    <rect class="bag" x="967" y="948" width="458" height="717" role="img" aria-label="Kraftpapier-Standbeutel"/>
    <rect class="bag-seam" x="967" y="948" width="458" height="8"/>
    <use href="#label-boxed" x="1069" y="948" width="256" height="357"/>
    <rect class="bag-window" x="1010" y="1340" width="375" height="135" role="img" aria-label="Cashewkerne im Sichtfenster"/>
  </g>
</svg>
</body>
</html>
```